Roadside building business signage for a holistic health clinic.

Replace signs as shown in the attached file. They are perforated stickers that go on the windows as shown. Looking for something that has our logo and says the name of the practice with logo (Fernbrook Health & Wellness) also boldly says Acupuncture, IV Vitamins, and Holistic Health.
Possibly our phone number as well 318-627-5194
Updates

Please don't use pink except the logo. Earthy, organic tone colors appreciated.

Need of eye catching window signage of a holistic clinic on a brick building. Pink, purple, sage green, white color. Logo is pink on a white background. Please don't overload with too much pink. Words to include are "Fernbrook Health and Wellness(name of business)", "Direct Primary Care", " Medical acupuncture", "IV Vitamin Therapy", "fernbrookcare-example.com","318-627-5194".

Target Market(s)

People will see in their cars passing by the building. Busy roadside so need to be visible while passing in fast speed.

Industry/Entity Type

Health & Wellness

Font styles to use
Sans Serif

Colors

Designer to choose colors to be used in the design.

Requirements
Must have
• On sign must have words Holistic Medicine, Medical Acupuncture, Direct Primary Care and IV vitamins.
Nice to have
• Simple, minimalistic, artistic yet has clear message. White, Black, Violet, Pink (logo), Dark green, Sage green.
Should not have
• Bold colors (red, yellow, blue), same tone colors. Blue waves on the current signage (uploaded file) must go.

```html
<!DOCTYPE html>
<html lang="en">
<head>
<meta charset="utf-8">
<title>Fernbrook Health &amp; Wellness — Window Signage Draft 3</title>
<link rel="stylesheet" href="https://fonts.googleapis.com/css2?family=Marcellus+SC&family=Oswald:wght@600&family=Arimo&display=swap">
<style>
  :root {
    --sky-blue: #629fc0;
    --forest: #2c5f57;
    --white: #ffffff;
    --board: #f1f1f1;
    --grey-text: #9a9a9a;
    --draft-band: #a6a6a6;
    --draft-text: #efefef;
    --logo-pink: #d9659b;
  }
  html, body {
    margin: 0;
    padding: 0;
    overflow: hidden;
  }
  body {
    width: 1200px;
    height: 1028px;
    background: var(--board);
    position: relative;
    font-family: "Arimo", Arial, sans-serif;
  }

  /* Signage strip */
  .sign-strip {
    position: absolute;
    left: 46px;
    top: 36px;
    width: 1099px;
    height: 272px;
    display: grid;
    grid-template-columns: repeat(4, 1fr);
    border: 2px solid var(--sky-blue);
    box-sizing: border-box;
    background: var(--white);
  }
  .sign-cell {
    position: relative;
    border-left: 2px solid var(--sky-blue);
  }
  .sign-cell:first-child { border-left: none; }

  .brand-block {
    position: absolute;
    left: 0;
    right: 0;
    top: 70px;
    text-align: center;
    color: var(--forest);
    font-family: "Marcellus SC", serif;
  }
  .brand-mark {
    width: 46px;
    height: 46px;
    border-radius: 50%;
    background: var(--logo-pink);
    margin: 0 auto 14px;
  }
  .brand-name {
    font-size: 28px;
    letter-spacing: 4px;
    line-height: 1;
  }
  .brand-tagline {
    font-size: 10px;
    letter-spacing: 3.6px;
    margin-top: 6px;
  }

  .service-line {
    position: absolute;
    left: 0;
    right: 0;
    text-align: center;
    font-family: "Marcellus SC", serif;
    font-size: 25px;
    letter-spacing: 2.2px;
    color: var(--forest);
    line-height: 1;
    transform: translateY(-50%);
    white-space: nowrap;
    -webkit-text-stroke: 0.6px var(--forest);
  }
  .service-line.tight { letter-spacing: 1px; }
  .service-rule {
    position: absolute;
    left: 11px;
    right: 11px;
    height: 2px;
    background: var(--sky-blue);
  }
  .phone-number {
    position: absolute;
    left: 0;
    right: 0;
    text-align: center;
    font-family: "Oswald", sans-serif;
    font-weight: 600;
    font-size: 46px;
    color: var(--forest);
    line-height: 1;
    transform: translateY(-50%) scaleY(1.05);
    letter-spacing: -0.5px;
  }

  /* Mockup area */
  .mockup-photo {
    position: absolute;
    left: 51px;
    top: 342px;
    width: 472px;
    height: 625px;
    background: linear-gradient(180deg, #8a7a72 0%, #8f5a4c 45%, #6f6a52 70%, #4b3c33 100%);
  }

  /* Palette */
  .palette-title {
    position: absolute;
    left: 588px;
    top: 352px;
    font-size: 34px;
    color: var(--grey-text);
    line-height: 1.2;
  }
  .swatch {
    position: absolute;
    top: 412px;
    width: 74px;
    height: 66px;
  }
  .swatch.sky { left: 583px; background: var(--sky-blue); }
  .swatch.white { left: 674px; background: var(--white); }
  .swatch.forest { left: 764px; background: var(--forest); }

  /* Draft notes */
  .draft-band {
    position: absolute;
    left: 664px;
    top: 529px;
    width: 536px;
    height: 124px;
    background: var(--draft-band);
    box-sizing: border-box;
    padding: 13px 0 0 16px;
    color: var(--draft-text);
    font-size: 28px;
    line-height: 32px;
  }
  .concept-notes {
    position: absolute;
    left: 680px;
    top: 659px;
    width: 510px;
    color: var(--grey-text);
    font-size: 20px;
    line-height: 23px;
  }
  .concept-notes p { margin: 0 0 22px; }
</style>
</head>
<body>

  <section class="sign-strip" aria-label="Window signage layout">
    <div class="sign-cell">
      <div class="brand-block">
        <div class="brand-mark"></div>
        <div class="brand-name">FERNBROOK</div>
        <div class="brand-tagline">HEALTH &amp; WELLNESS</div>
      </div>
    </div>

    <div class="sign-cell">
      <div class="service-line" style="top:38px">HOLISTIC</div>
      <div class="service-line" style="top:67px">MEDICINE</div>
      <div class="service-rule" style="top:91px"></div>
      <div class="service-line" style="top:117px">MEDICAL</div>
      <div class="service-line tight" style="top:156px">ACUPUNCTURE</div>
      <div class="service-rule" style="top:185px"></div>
      <div class="service-line" style="top:209px">DIRECT</div>
      <div class="service-line tight" style="top:248px">PRIMARY CARE</div>
    </div>

    <div class="sign-cell">
      <div class="brand-block">
        <div class="brand-mark"></div>
        <div class="brand-name">FERNBROOK</div>
        <div class="brand-tagline">HEALTH &amp; WELLNESS</div>
      </div>
    </div>

    <div class="sign-cell">
      <div class="service-line" style="top:90px">IV VITAMINS</div>
      <div class="service-rule" style="top:117px"></div>
      <div class="service-line" style="top:139px">HOLISTIC</div>
      <div class="service-line" style="top:178px">HEALTH</div>
      <div class="service-rule" style="top:205px"></div>
      <div class="phone-number" style="top:236px">318-627-5194</div>
    </div>
  </section>

  <div class="mockup-photo" role="img" aria-label="Photo of the brick clinic corner with the signage applied to its arched windows, sky pattern on the remaining panes"></div>

  <div class="palette-title">color scheme</div>
  <div class="swatch sky"></div>
  <div class="swatch white"></div>
  <div class="swatch forest"></div>

  <div class="draft-band">
    DRAFT 3:<br>
    Third version B for proof of concept<br>
    and the 3rd round of feedback
  </div>

  <div class="concept-notes">
    <p>Concept Design Description:<br>
    Using blue for the windows<br>
    (metal frame kept unchanged)</p>
    <p>To keep the central 4 squares in white<br>
    for the logo and the text to pop</p>
    <p>The use of a sky pattern for the windows<br>
    to bring serenity while also having something<br>
    visually attention grabbing</p>
  </div>

</body>
</html>
```